IT Company based on Biology Business Needs a Business Card Design

We need a business card design for a new company called 'Lumen CELL'. We develop the machine learning solutions especially focused on deep learning algorithms for biology industry. Our initial product is a vision detection on biological images to help doctors diagnose the symptoms. We would like to see designs that use the color green.

Industry/Entity Type

Business

```html
<!DOCTYPE html>
<html lang="en">
<head>
<meta charset="utf-8">
<title>Lumen CELL — Business Card</title>
<link href="https://fonts.googleapis.com/css2?family=Open+Sans:wght@400;600;700&family=Open+Sans+Condensed:wght@300;700&display=swap" rel="stylesheet">
<style>
  :root {
    --stage: #161616;
    --card: #ffffff;
    --leaf: #7dc242;
    --forest: #1e8a3c;
    --ink: #333333;
    --mist: #e3efd6;
  }
  html, body {
    margin: 0;
    width: 1200px;
    height: 900px;
    overflow: hidden;
    background: linear-gradient(#262626, #0a0a0a 80%);
    font-family: "Open Sans", Arial, sans-serif;
  }
  .card {
    position: absolute;
    top: 306px;
    width: 440px;
    height: 271px;
    background: var(--card);
    border-radius: 10px;
    overflow: hidden;
  }
  .card--front { left: 149px; }
  .card--back { left: 608px; }

  .brand {
    position: absolute;
    display: flex;
    align-items: center;
    gap: 10px;
    color: var(--leaf);
    font-weight: 600;
    letter-spacing: -1.5px;
    white-space: nowrap;
  }
  .brand__dot {
    width: 16px; height: 16px;
    border-radius: 50%;
    background: var(--forest);
    flex: none;
  }
  .card--front .brand { left: 40px; top: 114px; font-size: 32px; }
  .card--back .brand { left: 126px; top: 106px; font-size: 40px; }

  .contact {
    position: absolute;
    left: 262px;
    top: 60px;
    color: var(--ink);
    font-size: 12px;
    line-height: 16px;
  }
  .contact__name {
    margin: 0;
    color: var(--forest);
    font-size: 15px;
    font-weight: 700;
    line-height: 18px;
  }
  .contact__role { margin: 0 0 10px; font-size: 12.5px; }
  .contact__address { margin: 0 0 12px; font-style: normal; }
  .contact__list { list-style: none; margin: 0; padding: 0; }
  .contact__list li { display: flex; align-items: center; gap: 6px; }
  .contact__list svg { width: 9px; height: 9px; fill: var(--forest); flex: none; }

  .pattern {
    position: absolute;
    left: 0; top: 0;
    width: 140px; height: 100%;
    background: linear-gradient(90deg, var(--mist), rgba(227,239,214,0));
  }
</style>
</head>
<body>
  <section class="card card--front">
    <div class="brand"><span class="brand__dot"></span>Lumen CELL</div>
    <div class="contact">
      <p class="contact__name">Marcus Hale</p>
      <p class="contact__role">Managing Director</p>
      <address class="contact__address">48 Harbor Lane, Suite 12<br>Northfield, 204815.</address>
      <ul class="contact__list">
        <li><svg viewBox="0 0 10 10"><path d="M2 0l2 2.5-1.2 1.2c.6 1.3 1.6 2.3 2.9 2.9L7 5.3 10 7.2 8.8 9.6C4.3 9.4.6 5.7.4 1.2z"/></svg>044-555 210 384</li>
        <li><svg viewBox="0 0 10 10"><path d="M3 0h4a1 1 0 0 1 1 1v8a1 1 0 0 1-1 1H3a1 1 0 0 1-1-1V1a1 1 0 0 1 1-1zm.3 1.2v6.6h3.4V1.2z"/></svg>044-555 210 385</li>
        <li><svg viewBox="0 0 10 10"><path d="M0 2h10v6H0zm1 .8L5 5.6 9 2.8z" fill-rule="evenodd"/></svg>hello@lumencell.com</li>
        <li><svg viewBox="0 0 10 10"><circle cx="5" cy="5" r="4.6"/></svg>www.lumencell.com</li>
      </ul>
    </div>
  </section>

  <section class="card card--back">
    <div class="pattern" role="img" aria-label="Faint pale green brand pattern along the left edge"></div>
    <div class="brand"><span class="brand__dot"></span>Lumen CELL</div>
  </section>
</body>
</html>
```